Updated Stationary needed using new logo for Hair Tissue Mineral Analysis Company

Simple stationary design needed using new logo!
1. 8.5" x 11" Letterhead with company information listed below
2. 8.5" x 11" Design with Footer only with logo and information for print materials
3. 5.5" x 8.5" letterhead design
4. 4.125" x 9.5" Business envelope (#10 envelope) with address
5. 4.125" x 9.5" Business envelope with clear window (#10 envelope) with address
6. 6.5" x 9.5" envelope (6 3/4 Booklet envelope) with address
7. 10" x 13" Open End envelope
Address:
4817 N. Corwin Street
Phoenix, AZ 85021
Phone:
(602)-417-3926
Website:
www.pexumor.com
Email:
information@pexumor.com
Updates
Need extra days to review
Focused on completing other projects first
Look and feel
Each slider illustrates characteristics of the customer's brand and the style your logo design should communicate.

```html
<!DOCTYPE html>
<html lang="en">
<head>
<meta charset="utf-8">
<title>Pexumor Labs Letterhead</title>
<link href="https://fonts.googleapis.com/css2?family=Montserrat:wght@400;600;700&display=swap" rel="stylesheet">
<style>
  :root {
    --backdrop: #cbcbcb;
    --paper: #ffffff;
    --brand-blue: #2b56a0;
    --accent-orange: #f47b20;
    --ink: #2a2a2a;
    --watermark: #eceef6;
  }
  * { margin: 0; padding: 0; box-sizing: border-box; }
  html, body {
    width: 1200px; height: 923px; overflow: hidden;
    background: var(--backdrop);
    font-family: "Montserrat", sans-serif;
  }
  .letterhead {
    position: absolute;
    left: 259px; top: 20px;
    width: 683px; height: 883px;
    background: var(--paper);
    box-shadow: 0 6px 18px rgba(0,0,0,0.25);
  }
  .letterhead__brand {
    position: absolute;
    top: 30px; left: 0; right: 0;
    text-align: center;
  }
  .brand-name {
    display: inline-flex; align-items: center; gap: 10px;
    font-weight: 600; font-size: 26px; letter-spacing: 2px;
    color: var(--brand-blue);
  }
  .brand-name__dot {
    width: 12px; height: 12px; border-radius: 50%;
    background: var(--brand-blue);
  }
  .letterhead__watermark {
    position: absolute;
    top: 378px; left: 0; right: 0;
    text-align: center;
    font-weight: 700; font-size: 100px; letter-spacing: 4px;
    color: var(--watermark);
    line-height: 1;
    user-select: none;
  }
  .letterhead__footer {
    position: absolute;
    left: 0; right: 0; top: 818px;
    text-align: center;
    font-size: 12px; color: var(--ink);
    line-height: 21px;
  }
  .contact-line {
    display: flex; justify-content: center; align-items: center; gap: 6px;
  }
  .contact-item { display: inline-flex; align-items: center; gap: 4px; }
  .contact-icon { width: 9px; height: 9px; fill: var(--accent-orange); }
</style>
</head>
<body>
  <main class="letterhead">
    <header class="letterhead__brand">
      <span class="brand-name"><span class="brand-name__dot"></span>PEXUMOR LABS, INC.</span>
    </header>

    <div class="letterhead__watermark" aria-hidden="true">PEXUMOR</div>

    <footer class="letterhead__footer">
      <p class="address-line">4817 N. Corwin Street Phoenix, AZ 85021</p>
      <p class="contact-line">
        <span class="contact-item">
          <svg class="contact-icon" viewBox="0 0 10 10" aria-hidden="true"><path d="M1 3.5 Q5 0.5 9 3.5 L8 5 L6.5 4 L6.5 3.2 Q5 2.7 3.5 3.2 L3.5 4 L2 5 Z M2.5 5.5 H7.5 L8.5 9 H1.5 Z"/></svg>
          (602)-417-3926
        </span>
        <span class="contact-item">
          <svg class="contact-icon" viewBox="0 0 10 10" aria-hidden="true"><path d="M0.5 2 H9.5 V8.5 H0.5 Z" /><path d="M0.5 2 L5 5.5 L9.5 2" stroke="#fff" stroke-width="0.9" fill="none"/></svg>
          information@pexumor.com
        </span>
        <span class="contact-item">
          <svg class="contact-icon" viewBox="0 0 10 10" aria-hidden="true"><circle cx="5" cy="5" r="4.5"/><path d="M0.5 5 H9.5 M5 0.5 V9.5 M5 0.5 Q2 5 5 9.5 M5 0.5 Q8 5 5 9.5" stroke="#fff" stroke-width="0.7" fill="none"/></svg>
          www.pexumor.com
        </span>
      </p>
    </footer>
  </main>
</body>
</html>
```